Criação de Apres. Comercial (com dobra) para Limpeza & Serviço para o lar
A empresa queria:
" No mercado desde 2001, a Vento Sereno tem como Missão oferecer aos clientes a mais alta qualidade na prestação de serviço3s e manter a confiabilidade conquistada. Nosso posicionamento é o de parceria, no sentido de ajudar nossos clientes a viabilizar seus objetivos e projetos, mantendo-os focados em sua atividade principal. Serviços personalizados, com Mão-de-obra Terceirizada e bem treinada, acompanhados por constante Supervisão, de acordo com as necessidades e características de cada cliente, detectando pontos de melhoria e execução das tarefas de forma clara e precisa. Auxiliares de Serviços Gerais, Controladores de Acesso, Zeladores, Ascensoristas, Recepcionistas, Jardineiros, Copeiras, Garagistas, Limpadores de Vidro, Auxiliares de Manutenção, Telefonistas, Mensageiros, Auxiliares Administrativos. "

```html
<!DOCTYPE html>
<html lang="pt-BR">
<head>
<meta charset="UTF-8">
<title>Vento Sereno – Pasta Comercial</title>
<link href="https://fonts.googleapis.com/css2?family=Open+Sans:ital,wght@0,400;0,600;0,700;0,800;1,400;1,600;1,700&display=swap" rel="stylesheet">
<style>
  :root{
    --teal-dark:#1d5655;
    --teal:#22706d;
    --teal-mid:#2c8581;
    --teal-light:#3fb0a8;
    --paper:#ffffff;
    --stage:#e9ecec;
    --ink-soft:#cfe3e2;
  }
  *{margin:0;padding:0;box-sizing:border-box}
  html,body{width:1200px;height:1200px;overflow:hidden;background:var(--stage);font-family:"Open Sans",Arial,sans-serif}
  .folder{position:absolute;left:60px;top:220px;width:1080px;height:760px;display:flex;box-shadow:0 10px 30px rgba(0,0,0,.18)}
  .panel{position:relative;width:540px;height:760px;overflow:hidden}
  .panel-art{position:absolute;inset:0;width:100%;height:100%}

  /* back cover */
  .back{background:var(--teal-dark)}
  .map-area{position:absolute;left:60px;top:110px;width:330px;height:300px;border-radius:45% 55% 50% 40%;background:rgba(255,255,255,.045)}
  .contact{position:absolute;left:38px;top:440px;color:var(--paper)}
  .contact-title{font-style:italic;font-weight:700;font-size:19px;margin-bottom:12px}
  .contact-list{list-style:none;margin-left:-14px}
  .contact-item{display:flex;align-items:center;gap:12px;min-height:34px;padding:5px 0;border-bottom:1px solid rgba(255,255,255,.35);width:250px}
  .contact-icon{flex:0 0 24px;width:24px;height:24px;border-radius:4px;background:var(--paper);display:flex;align-items:center;justify-content:center}
  .contact-text{font-size:11px;font-style:italic;line-height:1.45;color:var(--ink-soft)}
  .web{position:absolute;font-style:italic;font-weight:600;color:var(--paper);font-size:16px;white-space:nowrap}
  .web strong{font-weight:800}
  .back .web{left:140px;bottom:18px}

  /* front cover */
  .front{background:var(--paper)}
  .brand{position:absolute;top:36px;left:0;width:100%;text-align:center}
  .brand-mark{width:48px;height:48px;border-radius:50%;background:var(--teal-mid);margin:0 auto 6px}
  .brand-name{font-weight:800;font-size:24px;color:var(--teal);line-height:1}
  .brand-sub{font-weight:600;font-size:10px;letter-spacing:4px;color:var(--teal);margin-top:4px}
  .tagline{position:absolute;top:236px;left:30px;width:510px;text-align:center;font-style:italic;font-weight:700;font-size:18px;line-height:24px;color:var(--teal)}
  .team-photo{position:absolute;left:30px;top:270px;width:510px;height:338px;background:linear-gradient(180deg,#f4f6f6 0%,#dde3e4 60%,#b9c3c5 100%)}
  .front .web{right:80px;bottom:22px;font-size:19px}
</style>
</head>
<body>
<div class="folder">

  <section class="panel back">
    <svg class="panel-art" viewBox="0 0 540 760" aria-hidden="true">
      <path d="M0 0H540V70Q300 130 0 80Z" fill="#2a6b69"/>
      <path d="M0 80Q300 130 540 70V76Q300 138 0 86Z" fill="#3a8f8a"/>
      <path d="M0 680Q260 650 540 585V760H0Z" fill="#ffffff"/>
      <path d="M0 700Q270 668 540 610V632Q270 690 0 720Z" fill="#3fb0a8"/>
      <path d="M0 722Q270 694 540 640V760H0Z" fill="#1d5655"/>
    </svg>
    <div class="map-area" role="img" aria-label="Mapa do Brasil em marca d'água"></div>

    <div class="contact">
      <h2 class="contact-title">Fale Conosco / Contato</h2>
      <ul class="contact-list">
        <li class="contact-item">
          <span class="contact-icon"><svg width="14" height="14" viewBox="0 0 14 14"><path d="M1 7L7 1.5 13 7H11V13H8.5V9H5.5V13H3V7Z" fill="#1d5655"/></svg></span>
          <span class="contact-text">Endereço: Rua das Acácias, 120 - Centro<br>São Paulo - SP / CEP 01000-000</span>
        </li>
        <li class="contact-item">
          <span class="contact-icon"><svg width="14" height="14" viewBox="0 0 14 14"><path d="M3 1.5L5.5 4 4.5 5.5Q5.8 8.3 8.5 9.5L10 8.5 12.5 11 11 12.8Q5 12 1.2 3Z" fill="#1d5655"/></svg></span>
          <span class="contact-text">(11) 3200-4510</span>
        </li>
        <li class="contact-item">
          <span class="contact-icon"><svg width="14" height="14" viewBox="0 0 14 14"><rect x="1.5" y="3" width="11" height="8" fill="none" stroke="#1d5655" stroke-width="1.4"/><path d="M1.5 3L7 8 12.5 3" fill="none" stroke="#1d5655" stroke-width="1.4"/></svg></span>
          <span class="contact-text">contato@ventosereno.com.br</span>
        </li>
      </ul>
    </div>

    <p class="web">www.<strong>ventosereno</strong>.com.br</p>
  </section>

  <section class="panel front">
    <svg class="panel-art" viewBox="0 0 540 760" aria-hidden="true">
      <path d="M0 150Q270 215 540 140V180Q270 240 0 182Z" fill="#22706d"/>
      <path d="M0 190Q270 245 540 188V194Q270 252 0 197Z" fill="#3fb0a8"/>
      <path d="M0 660Q280 630 540 612V624Q280 644 0 674Z" fill="#3fb0a8"/>
      <path d="M0 680Q280 650 540 632V760H0Z" fill="#22706d"/>
    </svg>

    <div class="brand">
      <div class="brand-mark"></div>
      <div class="brand-name">Vento Sereno</div>
      <div class="brand-sub">SERVIÇOS</div>
    </div>

    <p class="tagline">Serviços criados do seu jeito</p>
    <div class="team-photo" role="img" aria-label="Foto de equipe de profissionais de serviços gerais em ambiente de escritório"></div>

    <p class="web">www.<strong>ventosereno</strong>.com.br</p>
  </section>

</div>
</body>
</html>
```